Amber Ridge Productions

I need a business card design for a new freelance film production company using or incorporating the logo:
I want the card to be creative, minimal, yet professional. Feel free to use a variety of different shapes and sizes/ textures for the card.

Industry/Entity Type

Film Production

```html
<!DOCTYPE html>
<html lang="en">
<head>
<meta charset="utf-8">
<title>Amber Ridge Productions – Business Card</title>
<link rel="stylesheet" href="https://fonts.googleapis.com/css2?family=Jost:wght@400;500;600&family=Open+Sans:wght@400;600;700&display=swap">
<style>
  :root {
    --stage: #efebe6;
    --card: #e4dcd2;
    --card-edge: #d3c8bb;
    --brand-blue: #1553a8;
    --rule-grey: #7d7a78;
    --ink: #3e3a36;
    --ink-soft: #5a544e;
    --white: #ffffff;
  }
  * { box-sizing: border-box; margin: 0; padding: 0; }
  html, body { width: 1200px; height: 788px; overflow: hidden; }
  body {
    background: var(--stage);
    position: relative;
    font-family: "Open Sans", Arial, sans-serif;
    color: var(--ink);
  }
  .card {
    position: absolute;
    width: 525px;
    height: 300px;
    border-radius: 16px;
    background: var(--card);
    border: 1px solid var(--card-edge);
    overflow: hidden;
  }
  .card--front { left: 348px; top: 37px; }
  .card--back  { left: 60px;  top: 441px; }

  .card__band {
    position: absolute;
    left: 0; bottom: 0;
    width: 525px; height: 50px;
  }

  .brand {
    position: absolute;
    left: 0; right: 0; top: 52px;
    display: flex;
    flex-direction: column;
    align-items: center;
    gap: 14px;
  }
  .brand__mark {
    width: 34px; height: 34px;
    background: var(--brand-blue);
  }
  .brand__name {
    font-family: "Jost", "Futura", sans-serif;
    font-weight: 500;
    font-size: 27px;
    line-height: 1.05;
    color: var(--brand-blue);
    text-align: center;
    text-transform: uppercase;
    letter-spacing: 0.5px;
  }

  .contact {
    position: absolute;
    font-size: 13.5px;
    line-height: 18px;
    color: var(--ink-soft);
    list-style: none;
  }
  .contact li { display: flex; align-items: center; gap: 8px; white-space: nowrap; }
  .contact svg { width: 11px; height: 11px; fill: var(--brand-blue); flex: none; }
  .card--front .contact--lines { left: 102px; top: 172px; }
  .address {
    position: absolute;
    font-size: 13.5px;
    line-height: 18px;
    color: var(--ink-soft);
    font-style: normal;
  }
  .card--front .address { left: 295px; top: 208px; }

  .holder {
    position: absolute;
    left: 0; right: 0; bottom: 6px;
    text-align: center;
    color: var(--white);
    font-size: 14px;
  }
  .holder__name { font-weight: 700; font-size: 17px; }

  .card__mirror {
    position: absolute;
    inset: 0;
    transform: scaleX(-1);
    opacity: 0.85;
  }
  .card--back .contact--lines { left: 102px; top: 172px; }
  .card--back .address { left: 295px; top: 208px; }
  .card--back .brand { top: 30px; }

  .web {
    position: absolute;
    left: 0; right: 0; bottom: 9px;
    text-align: center;
    color: var(--white);
    font-size: 18px;
    letter-spacing: 0.2px;
  }
</style>
</head>
<body>

<svg width="0" height="0" style="position:absolute" aria-hidden="true">
  <defs>
    <symbol id="icon-phone" viewBox="0 0 12 12"><path d="M3 1l1.6 2.4-1 1.1c.6 1.3 1.6 2.3 2.9 2.9l1.1-1L10 8 9.2 10.2C5 10 2 7 1.8 2.8z"/></symbol>
    <symbol id="icon-mobile" viewBox="0 0 12 12"><rect x="3" y="0.5" width="6" height="11" rx="1"/><rect x="4" y="2" width="4" height="6" fill="#e4dcd2"/></symbol>
    <symbol id="icon-mail" viewBox="0 0 12 12"><rect x="0.5" y="2.5" width="11" height="7.5" rx="1"/><path d="M1 3l5 4 5-4" stroke="#e4dcd2" stroke-width="1" fill="none"/></symbol>
    <symbol id="icon-globe" viewBox="0 0 12 12"><circle cx="6" cy="6" r="5.5"/><path d="M0.5 6h11M6 0.5v11M2 3h8M2 9h8" stroke="#e4dcd2" stroke-width="0.8" fill="none"/></symbol>
  </defs>
</svg>

<!-- Front -->
<section class="card card--front" aria-label="Business card front">
  <div class="brand">
    <span class="brand__mark"></span>
    <p class="brand__name">Amber Ridge<br>Productions</p>
  </div>

  <ul class="contact contact--lines">
    <li><svg><use href="#icon-phone"/></svg>+12 345 67890</li>
    <li><svg><use href="#icon-mobile"/></svg>+12 345 67890</li>
    <li><svg><use href="#icon-mail"/></svg>info@website.com</li>
    <li><svg><use href="#icon-globe"/></svg>www.website.com</li>
  </ul>
  <address class="address">#0000, Street Name<br>Area Name, Country</address>

  <svg class="card__band" viewBox="0 0 525 50" preserveAspectRatio="none" aria-hidden="true">
    <path d="M0 17 Q260 -4 525 6" fill="none" stroke="var(--rule-grey)" stroke-width="3"/>
    <path d="M0 22 Q260 2 525 11 L525 50 L0 50 Z" fill="var(--brand-blue)"/>
  </svg>
  <p class="holder"><span class="holder__name">Your Name,</span> Designation</p>
</section>

<!-- Back -->
<section class="card card--back" aria-label="Business card back">
  <div class="card__mirror" aria-hidden="true">
    <div class="brand">
      <span class="brand__mark"></span>
      <p class="brand__name">Amber Ridge<br>Productions</p>
    </div>
    <ul class="contact contact--lines">
      <li><svg><use href="#icon-phone"/></svg>+12 345 67890</li>
      <li><svg><use href="#icon-mobile"/></svg>+12 345 67890</li>
      <li><svg><use href="#icon-mail"/></svg>info@website.com</li>
      <li><svg><use href="#icon-globe"/></svg>www.website.com</li>
    </ul>
    <address class="address">#0000, Street Name<br>Area Name, Country</address>
  </div>

  <svg class="card__band" viewBox="0 0 525 50" preserveAspectRatio="none" aria-hidden="true">
    <path d="M0 17 Q260 -4 525 6" fill="none" stroke="var(--rule-grey)" stroke-width="3"/>
    <path d="M0 22 Q260 2 525 11 L525 50 L0 50 Z" fill="var(--brand-blue)"/>
  </svg>
  <p class="web">www.website.com</p>
</section>

</body>
</html>
```